Tidecrest NZ Brand, Revenue, Promotions & Events

I need an innovative business card that pops my brand. I like the colours against darker gradients and i'm not afraid to be bold.

I run my own Business, Brand, Event & Promotion company. I specialise in breathing life into businesses and adding atmosphere to promotions and events. I am concept based lady that likes to test the boundaries and create stand out campaigns that connect with the consumer.

I have 12 years business experience in a realm of interesting fields form 11 years in coordinating international music festivals & promotions, 6 years in radio with 8 radio awards including a NZ radio award for best sales team in NZ and was the national brand and sales manager for New Zealands 1st indoor entertainment mall. With 10 years of experience in advertising sales, I have an eye for creating revenue streams for businesses and thrive on implementing campaigns that compliment those streams.

I love sayings like "Do what you love, love what you do" and believe that you can achieve anything you want.

I have been fortunate in my career that my connections have carried me without needing to promote my business however it is important that I start to do so.

Target Market(s)

Decision makers 25 to 54

Contact Information for Business Card

Petra Ollingham
Director
p. 022 587 3091
e. petra@tidecrest.nz
www.tidecrest.nz

FB, IG and Linkedin logo

Font styles to use
Sans Serif

Colors

Designer to choose colors to be used in the design.

Requirements
Must have
• Petra Ollingham
• Director
• p. 022 587 3091
• e. petra@tidecrest.nz
• www.tidecrest.nz
• FB, IG and Linkedin logo
Nice to have
• I am looking for a business card with character, that leaves my presence with my customer and makes them remember my brand & optimistic personality when i walk out the door.

```html
<!DOCTYPE html>
<html lang="en">
<head>
<meta charset="utf-8">
<title>Tidecrest NZ — Business Card</title>
<link rel="stylesheet" href="https://fonts.googleapis.com/css2?family=Lato:wght@400;700;900&display=swap">
<style>
  :root {
    --stage: #2b2724;
    --card-front: #0c0d0f;
    --card-back-top: #34465a;
    --card-back-bottom: #151d27;
    --brand-blue: #1fa3de;
    --text-grey: #b9bcc1;
    --rule-grey: #3a3d42;
    --tag-grey: #9aa3ad;
  }
  * { box-sizing: border-box; margin: 0; padding: 0; }
  html, body {
    width: 1200px; height: 844px; overflow: hidden;
    background: var(--stage);
    font-family: "Lato", Arial, sans-serif;
  }
  .stage {
    position: relative; width: 1200px; height: 844px;
    display: flex; align-items: center; justify-content: center; gap: 40px;
  }
  .card {
    width: 525px; height: 300px; position: relative;
    box-shadow: 0 12px 30px rgba(0,0,0,.45);
    display: flex; flex-direction: column; align-items: center;
    overflow: hidden;
  }
  .card--front { background: var(--card-front); padding-top: 62px; }
  .card--back { justify-content: center; }

  .back-photo {
    position: absolute; inset: 0;
    background: linear-gradient(160deg, var(--card-back-top) 0%, #243242 50%, var(--card-back-bottom) 100%);
  }

  .brand { display: flex; flex-direction: column; align-items: center; position: relative; }
  .brand__row { display: flex; align-items: center; gap: 10px; }
  .brand__dot { width: 16px; height: 16px; border-radius: 50%; background: var(--brand-blue); }
  .brand__name {
    font-weight: 700; font-size: 34px; letter-spacing: 3px;
    color: var(--brand-blue); line-height: 1;
  }
  .brand__tagline {
    margin-top: 6px; font-size: 11.5px; letter-spacing: 1.2px;
    color: var(--tag-grey); text-transform: uppercase;
  }

  .person { margin-top: 22px; text-align: center; }
  .person__name {
    font-weight: 900; font-size: 18px; letter-spacing: .5px;
    color: var(--brand-blue); text-transform: uppercase;
  }
  .person__title { font-size: 13px; color: var(--text-grey); margin-top: 1px; }

  .rule { width: 250px; height: 1px; background: var(--rule-grey); margin: 10px 0; }

  .contact { font-size: 13.5px; color: var(--text-grey); white-space: nowrap; }
  .contact__label { color: var(--brand-blue); font-weight: 700; }

  .social { display: flex; gap: 6px; margin-top: 9px; }
  .social__item {
    width: 18px; height: 18px; border-radius: 50%;
    border: 1.4px solid var(--text-grey);
  }

  .motto {
    position: relative; margin-top: 44px;
    font-size: 12px; letter-spacing: 1.4px; color: #c9d2dc; text-transform: uppercase;
  }
  .card--back .brand__name { color: #6cc6f0; }
</style>
</head>
<body>
<main class="stage">
  <section class="card card--front" aria-label="Business card front">
    <div class="brand">
      <div class="brand__row">
        <span class="brand__dot"></span>
        <span class="brand__name">TIDECREST NZ</span>
      </div>
      <p class="brand__tagline">Brand | Revenue | Events &amp; Promotions</p>
    </div>
    <div class="person">
      <h1 class="person__name">Petra Ollingham</h1>
      <p class="person__title">Director</p>
    </div>
    <div class="rule"></div>
    <p class="contact">
      <span class="contact__label">P:</span> 022 587 3091 |
      <span class="contact__label">E:</span> petra@tidecrest.nz | www.<span class="contact__label" style="font-weight:400">tidecrest</span>.nz
    </p>
    <div class="social" aria-label="Social profiles">
      <span class="social__item"></span>
      <span class="social__item"></span>
      <span class="social__item"></span>
    </div>
    <div class="rule"></div>
  </section>

  <section class="card card--back" aria-label="Business card back">
    <div class="back-photo" role="img" aria-label="Faint blue-toned photo of a modern office interior"></div>
    <div class="brand">
      <div class="brand__row">
        <span class="brand__dot"></span>
        <span class="brand__name">TIDECREST NZ</span>
      </div>
      <p class="brand__tagline">Brand | Revenue | Events &amp; Promotions</p>
    </div>
    <p class="motto">Do what you love, love what you do</p>
  </section>
</main>
</body>
</html>
```